create a more innovative version of our powerpoint presentation

We built A 14-pages powerpoint document. We would like to change the look of this document. We work in digital area. So, we would like something more modern, more current and less classical. We need to be fashionable while remaining reassuring for corporate. Our business is to make recommendations in 5 days where our competitors do it in 3 months and after to support companies with this "vane'spark" proposition.

Target Market(s)

medium sized business, or a large global enterprise

Industry/Entity Type

Digital

Colors

Designer to choose colors to be used in the design.

Requirements
Must have
• We are working with digital expert. We need to surprise them.

```html
<!DOCTYPE html>
<html lang="fr">
<head>
<meta charset="utf-8">
<title>Shift Forward – Présentation</title>
<link rel="stylesheet" href="https://fonts.googleapis.com/css2?family=PT+Sans:wght@400;700&display=swap">
<style>
  :root{
    --teal:#2bb0ad;
    --teal-light:#4cc6c2;
    --teal-dark:#1e8f8c;
    --orange:#f2a65e;
    --orange-dark:#c9782f;
    --navy:#1b2160;
    --white:#ffffff;
    --page:#f4f4f4;
    --muted:#a9a9a9;
    --rule:#e6e6e6;
  }
  *{box-sizing:border-box;margin:0;padding:0}
  html,body{width:1200px;height:3000px;overflow:hidden}
  body{background:var(--page);font-family:"PT Sans",Arial,sans-serif;position:relative}

  .slide{position:absolute;left:12px;width:1176px;height:664px;background:var(--white);
    box-shadow:0 4px 10px rgba(0,0,0,.28);overflow:hidden}
  .slide--cover{top:44px}
  .slide--photo{top:794px}
  .slide--pillars{top:1542px}
  .slide--world{top:2294px}

  /* brand mark */
  .brand{position:absolute;background:var(--white);display:flex;align-items:center;gap:10px;
    padding:0 22px;color:var(--navy);font-weight:700;z-index:3}
  .brand__square{width:18px;height:18px;background:var(--orange);flex:none}
  .brand--cover{right:56px;top:32px;height:160px;font-size:30px}
  .brand--photo{left:58px;top:36px;height:156px;font-size:30px}
  .brand--footer{left:60px;bottom:22px;height:40px;font-size:17px;padding:0;gap:7px}
  .brand--footer .brand__square{width:11px;height:11px}

  /* cover */
  .band{position:absolute;left:0;right:0;top:152px;bottom:0;background:var(--teal)}
  .slide--photo .band{top:152px}
  .cover-art{position:absolute;left:140px;top:250px;width:230px;height:230px;
    background:radial-gradient(circle,rgba(255,255,255,.25),rgba(255,255,255,0) 70%)}
  .cover-title{position:absolute;left:452px;top:232px;color:var(--white);font-weight:700;
    font-size:68px;line-height:80px}

  /* photo cover */
  .photo-bg{position:absolute;inset:0;
    background:linear-gradient(100deg,#2a9d9a 0%,#5cc9c5 30%,#3fbab6 55%,#48c1bd 100%)}
  .photo-title{position:absolute;left:502px;top:104px;color:var(--white);font-weight:700;
    font-size:58px;line-height:72px;z-index:2}

  /* content slides */
  .tab{position:absolute;left:500px;top:0;width:176px;height:14px;background:var(--orange)}
  .slide-title{position:absolute;left:0;right:0;top:38px;text-align:center;color:var(--navy);
    font-weight:700;font-size:42px}

  .pillar{position:absolute;left:0;width:988px;height:84px}
  .pillar--1{top:172px}.pillar--2{top:290px}.pillar--3{top:408px}
  .pillar__arrow{position:absolute;left:0;top:0;width:988px;height:84px;
    clip-path:polygon(0 0,952px 0,100% 50%,952px 100%,0 100%);background:var(--teal-light)}
  .pillar--2 .pillar__arrow{background:var(--orange);opacity:.9}
  .pillar__label{position:absolute;left:0;top:-16px;width:254px;height:84px;background:var(--teal);
    color:var(--white);font-weight:700;font-size:22px;line-height:26px;text-align:center;
    display:flex;align-items:center;justify-content:center}
  .pillar--2 .pillar__label{background:var(--orange)}
  .pillar__fold{position:absolute;left:234px;top:68px;width:20px;height:16px;
    background:var(--teal-dark);clip-path:polygon(0 0,100% 0,100% 100%)}
  .pillar--2 .pillar__fold{background:var(--orange-dark)}
  .pillar__items{position:absolute;left:326px;top:0;height:84px;display:flex;flex-direction:column;
    justify-content:center;list-style:none;color:var(--white);font-size:21px;line-height:30px}
  .pillar__items li::before{content:"▪";font-size:12px;margin-right:14px;vertical-align:3px}

  .footer{position:absolute;left:0;right:0;bottom:0;height:84px}
  .footer__rule{position:absolute;left:168px;right:90px;top:28px;height:2px;background:var(--rule)}
  .footer__meta{position:absolute;left:0;right:0;top:42px;text-align:center;color:var(--muted);font-size:13px;word-spacing:4px}
  .footer__page{position:absolute;right:56px;top:38px;color:var(--teal);font-weight:700;font-size:22px}

  .cloud{position:absolute;left:364px;top:118px;width:448px;height:448px;border-radius:50%;
    background:radial-gradient(circle at 45% 40%,#e8eef2 0%,#c9d7df 55%,#b9cbd6 100%)}
</style>
</head>
<body>

<section class="slide slide--cover">
  <div class="brand brand--cover"><span>Shift Forward</span><span class="brand__square"></span></div>
  <div class="band"></div>
  <div class="cover-art" role="img" aria-label="Dessin au trait d'un personnage élancé en mouvement vers l'avant"></div>
  <h1 class="cover-title">Accompagner la<br>Transformation<br>des personnes et<br>des organisations</h1>
</section>

<section class="slide slide--photo">
  <div class="brand brand--photo"><span class="brand__square"></span><span>Shift Forward</span></div>
  <div class="band">
    <div class="photo-bg" role="img" aria-label="Photo teintée turquoise d'une main touchant un écran, avec un réseau de points reliés"></div>
    <h1 class="photo-title">Accompagner la<br>Transformation<br>des personnes et des<br>organisations</h1>
  </div>
</section>

<section class="slide slide--pillars">
  <div class="tab"></div>
  <h2 class="slide-title">Shift Forward</h2>

  <div class="pillar pillar--1">
    <div class="pillar__arrow"></div>
    <div class="pillar__label">Evoluer<br>autrement</div>
    <div class="pillar__fold"></div>
    <ul class="pillar__items"><li>Anticiper</li><li>Ré-inventer</li></ul>
  </div>
  <div class="pillar pillar--2">
    <div class="pillar__arrow"></div>
    <div class="pillar__label">Avec la Marque</div>
    <div class="pillar__fold"></div>
    <ul class="pillar__items"><li>comme point d'appui</li></ul>
  </div>
  <div class="pillar pillar--3">
    <div class="pillar__arrow"></div>
    <div class="pillar__label">Pour<br>accompagner</div>
    <div class="pillar__fold"></div>
    <ul class="pillar__items"><li>Les Personnes</li><li>Et les Organisations</li></ul>
  </div>

  <footer class="footer">
    <div class="brand brand--footer"><span class="brand__square"></span><span>Shift Forward</span></div>
    <div class="footer__rule"></div>
    <div class="footer__meta">10/02/2018 | SFW</div>
    <div class="footer__page">3</div>
  </footer>
</section>

<section class="slide slide--world">
  <div class="tab"></div>
  <h2 class="slide-title">Le monde se transforme inexorablement!</h2>
  <div class="cloud" role="img" aria-label="Nuage de mots circulaire : Design, Start Up, Big Data, Cloud, Agilité, Innovation, Coworking, Intelligence Artificielle"></div>
  <footer class="footer">
    <div class="brand brand--footer"><span class="brand__square"></span><span>Shift Forward</span></div>
    <div class="footer__rule"></div>
    <div class="footer__meta">10/02/2018 | SFW</div>
    <div class="footer__page">4</div>
  </footer>
</section>

</body>
</html>
```